Warehouse fit out company needed website design!

Colour scheme to match attached business logo (faded lemon yellow, charcoal and white.

My business is doing warehouse fit outs using heavy duty storage systems such as pallet racking, mezzanine floors, cantilever racking and shelving.

Website to be modern style and easy for the customer to navigate through.

Please visit this competitors website for example of the type of design I would like www.brindlevault.com.au

My business will be providing the exact same service and products so this will give you a great understanding of what I am chasing from my website

Target Market(s)

Small to large businesses with warehouses to store their product.

Coding

Coded - Design and coding required

Number of Pages Required

5+ page

Colors
fbed22
ffffff
1b1b1b

Requirements
Must have
• Bold banner incorporating my attached logo on each page with drop boxes for products, services, contact us
• Home page to have "about us" write up section and images
Nice to have
• Modern style layout and easy to navigate through for the client

```html
<!DOCTYPE html>
<html lang="en">
<head>
<meta charset="utf-8">
<title>Rackwell Storage — Warehouse Storage Equipment</title>
<link rel="stylesheet" href="https://fonts.googleapis.com/css2?family=Lato:wght@300;400;700;900&display=swap">
<style>
:root{
  --lemon:#f0ec4a;
  --lemon-strong:#fbed22;
  --charcoal:#3a3a3a;
  --ink:#1b1b1b;
  --white:#ffffff;
  --grey-text:#8a8a8a;
  --rule:#e6e6e6;
  --footer:#3a3a3a;
}
*{box-sizing:border-box;margin:0;padding:0}
html,body{width:1200px;height:3396px;overflow:hidden}
body{position:relative;font-family:'Lato',sans-serif;color:var(--ink);background:var(--white)}
.abs{position:absolute}
a{text-decoration:none;color:inherit}

/* header */
.site-header{left:0;top:0;width:1200px;height:70px;background:var(--lemon)}
.brand{left:72px;top:14px;font-weight:900;font-size:30px;letter-spacing:2px;color:var(--charcoal);line-height:42px}
.main-nav{left:419px;top:24px;display:flex;gap:30px;font-size:18px;color:#6b6b3a}
.header-cta{left:982px;top:15px;width:145px;height:39px;background:var(--charcoal);color:var(--white);border-radius:3px;font-size:19px;display:flex;align-items:center;justify-content:center}

/* hero */
.hero-photo{left:0;top:70px;width:1200px;height:633px;background:linear-gradient(100deg,#59616a 0%,#8c8f93 35%,#b39b78 65%,#c7a982 85%,#98918a 100%)}
.hero-panel{left:74px;top:189px;width:526px;height:395px;background:rgba(50,50,50,.88)}
.hero-title{left:123px;top:232px;width:450px;font-size:42px;font-weight:700;line-height:49px;color:var(--white)}
.hero-text{left:123px;top:394px;width:440px;font-size:19px;line-height:28px;color:var(--white)}
.btn{display:flex;align-items:center;justify-content:center;font-weight:700;border-radius:3px}
.btn-lemon{background:var(--lemon);color:var(--charcoal)}
.hero-cta{left:123px;top:487px;width:207px;height:50px;font-size:22px}
.text-link{font-size:22px;display:flex;align-items:center;gap:8px}
.hero-link{left:360px;top:495px;color:#d9d9d9;height:34px}

/* about */
.photo{background:linear-gradient(160deg,#9aa3ad,#7f8791 60%,#a08c6a)}
.photo-tall{left:74px;top:815px;width:249px;height:509px}
.photo-top{left:341px;top:815px;width:250px;height:245px;background:linear-gradient(200deg,#b89c74,#8e97a2 55%,#9aa3ad)}
.photo-bottom{left:341px;top:1079px;width:250px;height:245px;background:linear-gradient(170deg,#c2a783,#939ca6 55%,#8c949e)}
.section-title{font-size:42px;font-weight:700;text-transform:uppercase;color:var(--charcoal);line-height:49px}
.accent{color:var(--lemon);font-style:italic}
.about-title{left:695px;top:822px;width:440px}
.about-text{left:695px;top:990px;width:430px;font-size:19px;line-height:28px;color:var(--grey-text);font-weight:300}
.about-cta{left:695px;top:1259px;width:206px;height:50px;font-size:22px}
.about-link{left:931px;top:1267px;color:var(--charcoal);height:34px}

/* why */
.why{left:0;top:1440px;width:1200px;height:703px;background:linear-gradient(180deg,#ecea4e,#eeeb5a 50%,#e8e34a)}
.why-title{left:0;top:1512px;width:1200px;text-align:center}
.why-title .accent{color:var(--white)}
.feature{top:1604px;width:310px;height:353px;background:var(--white);text-align:center}
.feature-icon{position:absolute;left:96px;top:38px;width:119px;height:119px;border-radius:50%;background:var(--charcoal);display:flex;align-items:center;justify-content:center}
.feature h3{position:absolute;left:0;top:180px;width:100%;font-size:21px;font-weight:400;color:var(--ink)}
.feature p{position:absolute;left:28px;top:215px;width:254px;font-size:14.5px;line-height:23px;color:var(--grey-text);font-weight:300}
.why-btn{top:2008px;width:265px;height:62px;font-size:24px}
.btn-dark{left:322px;background:var(--charcoal);color:var(--white)}
.btn-outline{left:614px;border:2px solid var(--charcoal);color:var(--charcoal)}

/* faq */
.faq-title{left:0;top:2239px;width:1200px;text-align:center}
.faq-item{left:141px;width:921px;border-bottom:1.5px solid var(--rule)}
.faq-q{position:absolute;left:21px;font-size:21px;color:var(--ink)}
.faq-chevron{position:absolute;right:30px}
.faq-a{position:absolute;left:18px;top:48px;width:880px;font-size:15px;line-height:24px;color:var(--grey-text);font-weight:300}
.faq-cta{left:368px;top:2943px;width:265px;height:62px;font-size:24px}
.faq-link{left:709px;top:2957px;color:#6b6b6b;font-size:24px;height:34px}

/* footer */
.site-footer{left:0;top:3149px;width:1200px;height:247px;background:var(--footer)}
.footer-brand{left:72px;top:3202px;font-size:48px;font-weight:900;letter-spacing:3px;color:var(--lemon);line-height:56px}
.copyright{left:72px;top:3342px;font-size:12px;color:#e0e0e0}
.footer-col{top:3210px}
.footer-col h4{font-size:11px;letter-spacing:2.5px;font-weight:700;color:#e8e8e8;margin-bottom:16px}
.footer-col li{list-style:none;font-size:12px;color:#7c7c7c;line-height:32px}
</style>
</head>
<body>

<header class="abs site-header"></header>
<div class="abs brand">RACKWELL</div>
<nav class="abs main-nav"><a href="#">Services</a><a href="#">Products</a><a href="#">About Us</a><a href="#">FAQs</a></nav>
<a class="abs header-cta" href="#">Contact Us</a>

<section>
  <div class="abs hero-photo" role="img" aria-label="Warehouse interior with tall pallet racking, stacked boxes and wooden crates"></div>
  <div class="abs hero-panel"></div>
  <h1 class="abs hero-title">We Designs, Supplies &amp; Installs Warehouse Storage Equipments</h1>
  <p class="abs hero-text">Lorem ipsum dolor sit amet, consectetur adipiscing elit. Sed malesuada.</p>
  <a class="abs btn btn-lemon hero-cta" href="#">Contact Us</a>
  <a class="abs text-link hero-link" href="#">Learn More <svg width="16" height="12" viewBox="0 0 16 12"><path d="M1 6h13M9 1l5 5-5 5" fill="none" stroke="#d9d9d9" stroke-width="1.6"/></svg></a>
</section>

<section>
  <div class="abs photo photo-tall" role="img" aria-label="Overhead view of a warehouse worker in hard hat beside stacked boxes"></div>
  <div class="abs photo photo-top" role="img" aria-label="Overhead view of boxes on shelving and a pallet jack"></div>
  <div class="abs photo photo-bottom" role="img" aria-label="Overhead view of cardboard boxes on a concrete floor"></div>
  <h2 class="abs section-title about-title">We are <span class="accent">leading</span> the warehouse storage industry</h2>
  <p class="abs about-text">Lorem ipsum dolor sit amet, consectetur adipiscing elit. Praesent metus justo, sodales id felis ac, pharetra finibus mi. Orci varius natoque penatibus et magnis dis parturient montes, nascetur ridiculus mus. Integer sed finibus odio. Praesent eros leo, finibus et mauris non, tristique aliquam urna. Donec sed arcu ut arcu laoreet mattis. Sed rhoncus felis enim, et consectetur.</p>
  <a class="abs btn btn-lemon about-cta" href="#">Contact Us</a>
  <a class="abs text-link about-link" href="#">Learn More <svg width="16" height="12" viewBox="0 0 16 12"><path d="M1 6h13M9 1l5 5-5 5" fill="none" stroke="#3a3a3a" stroke-width="1.6"/></svg></a>
</section>

<section>
  <div class="abs why" role="img" aria-label="Warehouse racking background washed in lemon yellow"></div>
  <h2 class="abs section-title why-title">Why <span class="accent">you</span> choose us</h2>

  <article class="abs feature" style="left:74px">
    <div class="feature-icon"><svg width="56" height="56" viewBox="0 0 56 56" fill="none" stroke="#f0ec4a" stroke-width="2"><circle cx="28" cy="22" r="15"/><circle cx="28" cy="22" r="10"/><path d="M28 16l2 4.5 4.8.4-3.7 3.1 1.2 4.7L28 26.2l-4.3 2.5 1.2-4.7-3.7-3.1 4.8-.4z"/><path d="M19 34l-6 16 6-3 3 5 5-14M37 34l6 16-6-3-3 5-5-14"/></svg></div>
    <h3>High Quality Products</h3>
    <p>Class aptent taciti sociosqu ad litora torquent per conubia nostra, per inceptos himenaeos. Nulla ultrices, quam eu imperdiet pulvinar,</p>
  </article>

  <article class="abs feature" style="left:446px">
    <div class="feature-icon"><svg width="56" height="56" viewBox="0 0 56 56" fill="none" stroke="#f0ec4a" stroke-width="2"><circle cx="22" cy="28" r="8"/><path d="M12 26c0-8 5-12 10-12s10 4 10 12"/><path d="M8 50c2-8 7-12 14-12s12 4 14 12z"/><circle cx="42" cy="14" r="8"/><path d="M42 11v1M42 14v5M36 20l-3 4"/></svg></div>
    <h3>Excellent Client Services</h3>
    <p>Class aptent taciti sociosqu ad litora torquent per conubia nostra, per inceptos himenaeos. Nulla ultrices, quam eu imperdiet pulvinar,</p>
  </article>

  <article class="abs feature" style="left:817px">
    <div class="feature-icon"><svg width="56" height="56" viewBox="0 0 56 56" fill="none" stroke="#f0ec4a" stroke-width="2"><rect x="6" y="8" width="44" height="30"/><rect x="10" y="12" width="36" height="22"/><path d="M14 30l8-8 6 5 10-11"/><circle cx="22" cy="22" r="1.5"/><circle cx="28" cy="27" r="1.5"/><circle cx="38" cy="16" r="1.5"/><path d="M28 38v8M18 48h20"/></svg></div>
    <h3>Years of Experience</h3>
    <p>Class aptent taciti sociosqu ad litora torquent per conubia nostra, per inceptos himenaeos. Nulla ultrices, quam eu imperdiet pulvinar,</p>
  </article>

  <a class="abs btn btn-dark why-btn" href="#">Our Services</a>
  <a class="abs btn btn-outline why-btn" href="#">Our Products</a>
</section>

<section>
  <h2 class="abs section-title faq-title">Frequently <span class="accent">asked</span> questions</h2>

  <div class="abs faq-item" style="top:2325px;height:159px">
    <span class="faq-q" style="top:18px">The First Question most customers Asks?</span>
    <svg class="faq-chevron" style="top:24px" width="22" height="14" viewBox="0 0 22 14"><path d="M2 12l9-9 9 9" fill="none" stroke="#f0ec4a" stroke-width="3"/></svg>
    <p class="faq-a">Lorem ipsum dolor sit amet, consectetur adipiscing elit. Praesent metus justo, sodales id felis ac, pharetra finibus mi. Orci varius natoque penatibus et magnis dis parturient montes, nascetur ridiculus mus. Integer sed finibus odio. Praesent eros leo, finibus et mauris non, tristique aliquam urna. Donec sed arcu ut arcu laoreet mattis.</p>
  </div>
  <div class="abs faq-item" style="top:2484px;height:85px">
    <span class="faq-q" style="top:28px">The Second Question most customers Asks?</span>
    <svg class="faq-chevron" style="top:34px" width="22" height="14" viewBox="0 0 22 14"><path d="M2 2l9 9 9-9" fill="none" stroke="#f0ec4a" stroke-width="3"/></svg>
  </div>
  <div class="abs faq-item" style="top:2569px;height:83px">
    <span class="faq-q" style="top:26px">The Third Question most customers Asks?</span>
    <svg class="faq-chevron" style="top:32px" width="22" height="14" viewBox="0 0 22 14"><path d="M2 2l9 9 9-9" fill="none" stroke="#f0ec4a" stroke-width="3"/></svg>
  </div>
  <div class="abs faq-item" style="top:2652px;height:84px">
    <span class="faq-q" style="top:26px">The Fourth Question most customers Asks?</span>
    <svg class="faq-chevron" style="top:32px" width="22" height="14" viewBox="0 0 22 14"><path d="M2 2l9 9 9-9" fill="none" stroke="#f0ec4a" stroke-width="3"/></svg>
  </div>
  <div class="abs faq-item" style="top:2736px;height:83px">
    <span class="faq-q" style="top:26px">The Fifth Question most customers Asks?</span>
    <svg class="faq-chevron" style="top:32px" width="22" height="14" viewBox="0 0 22 14"><path d="M2 2l9 9 9-9" fill="none" stroke="#f0ec4a" stroke-width="3"/></svg>
  </div>
  <div class="abs faq-item" style="top:2819px;height:84px;border-bottom:none">
    <span class="faq-q" style="top:28px">The Sixth Question most customers Asks?</span>
    <svg class="faq-chevron" style="top:34px" width="22" height="14" viewBox="0 0 22 14"><path d="M2 2l9 9 9-9" fill="none" stroke="#f0ec4a" stroke-width="3"/></svg>
  </div>

  <a class="abs btn btn-lemon faq-cta" href="#">Contact Us</a>
  <a class="abs text-link faq-link" href="#">View All <svg width="22" height="14" viewBox="0 0 22 14"><path d="M1 7h19M14 1l6 6-6 6" fill="none" stroke="#6b6b6b" stroke-width="1.8"/></svg></a>
</section>

<footer class="abs site-footer"></footer>
<div class="abs footer-brand">RACKWELL</div>
<p class="abs copyright">© 2019 Rackwell Storage. All rights reserved.</p>
<div class="abs footer-col" style="left:603px"><h4>LEARN MORE</h4><ul><li>Home</li><li>Products</li><li>Testimonials</li></ul></div>
<div class="abs footer-col" style="left:815px"><h4>INFORMATION</h4><ul><li>About Us</li><li>FAQs</li><li>Privacy Policy</li><li>Terms &amp; Conditions</li></ul></div>
<div class="abs footer-col" style="left:1026px"><h4>GET IN TOUCH</h4><ul><li>Contact Us</li><li>Customer Service</li></ul></div>

</body>
</html>
```